Agriculture Technology Website Design Project

We need a new website for a company called Brook Ledger Works. We have a document laid out with all of the requirements (see below) and would like you to follow the instructions on there. In this document, there is all of the copy that must be included on the website and what order it should go in as well as images. These images have specific names and are listed in the document as to where they should go. Please make this one continuous site that users can easily scroll through. We would like it to be sleek and modern with as little clutter as possible. Please refer to the brochure that we have posted below (Stone Analytica.pdf) for a design we have had done for the company in the past. We really like this design and it would be great if the color scheme was similar on the website.

Industry/Entity Type

Agriculture

Number of Pages Required

1 page

Font styles to use
Sans Serif

```html
<!DOCTYPE html>
<html lang="en">
<head>
<meta charset="utf-8">
<title>Brook Ledger Works</title>
<link rel="stylesheet" href="https://fonts.googleapis.com/css2?family=Poppins:wght@300;400;500;600;700&display=swap">
<style>
:root{
  --green:#2c8a0c;
  --green-dark:#1f6d05;
  --green-pale:#d6e9cf;
  --ink:#222;
  --muted:#666;
  --white:#fff;
  --hero-dark:#1c2419;
}
*{margin:0;padding:0;box-sizing:border-box}
html,body{width:1200px;height:4693px;overflow:hidden}
body{font-family:"Poppins",sans-serif;color:var(--ink);background:var(--white);position:relative}
.abs{position:absolute}
.btn{position:absolute;display:flex;align-items:center;justify-content:center;background:var(--green);color:var(--white);border-radius:30px;font-size:20px;font-weight:500;text-decoration:none}

/* hero */
.hero{position:absolute;left:0;top:0;width:1200px;height:700px;background:linear-gradient(180deg,#2a3227 0%,#1e281b 45%,#26401a 75%,#2f4d1c 100%)}
.hero-photo{position:absolute;inset:0;background:radial-gradient(ellipse at 60% 20%,rgba(120,140,120,.35),transparent 60%),radial-gradient(ellipse at 30% 80%,rgba(70,110,40,.5),transparent 60%)}
.brand{position:absolute;left:76px;top:52px;display:flex;align-items:center;gap:8px;color:var(--green);font-size:15px;font-weight:500}
.brand i{width:18px;height:18px;border-radius:50%;background:var(--green);display:block}
.nav{position:absolute;right:80px;top:30px;display:flex;gap:22px;font-size:14px;color:var(--white)}
.nav a{color:var(--white);text-decoration:none;height:24px;line-height:24px}
.nav-active{position:absolute;left:526px;top:-40px;width:130px;height:110px;border-radius:50%;background:var(--green)}
.hero-title{position:absolute;top:240px;width:1200px;text-align:center;color:var(--white);font-size:50px;font-weight:700;letter-spacing:1px}
.hero-title span{color:var(--green)}
.hero-sub{position:absolute;top:306px;width:1200px;text-align:center;color:var(--white);font-size:18px}

/* services */
.seed-mark{position:absolute;left:584px;top:712px;width:32px;height:32px;border-radius:50%;background:var(--green)}
.service{position:absolute;top:823px;width:200px;text-align:center}
.service .ic{width:94px;height:94px;border-radius:50%;background:var(--green);margin:0 auto;display:flex;align-items:center;justify-content:center}
.service.on .ic{box-shadow:0 0 0 6px var(--white),0 0 0 8px var(--green)}
.service h3{margin-top:50px;font-size:15px;font-weight:500;line-height:25px;text-transform:uppercase}
.service.on h3{color:var(--green)}
.service p{margin:14px auto 0;width:184px;font-size:14px;line-height:25px;color:var(--muted)}

h2.sec{color:var(--green);font-weight:600;font-size:38px;line-height:46px}
.lead{font-size:17px;line-height:27px}
.copy{font-size:14px;line-height:27px;color:var(--muted)}

.ph{position:absolute}
</style>
</head>
<body>

<header class="hero">
  <div class="hero-photo" role="img" aria-label="Sprinklers watering a green field at dusk"></div>
  <div class="brand"><i></i>BROOK LEDGER WORKS</div>
  <div class="nav-active"></div>
  <nav class="nav">
    <a href="#">HOME</a><a href="#">ABOUT US</a><a href="#">WHY BLW ?</a><a href="#">PRODUCTS</a><a href="#">PARTNERS</a><a href="#">CONTACT US</a>
  </nav>
  <h1 class="hero-title">BROOK <span>LEDGER</span> WORKS</h1>
  <p class="hero-sub">Bringing industrial automation to the farm</p>
  <a class="btn" href="#" style="left:506px;top:351px;width:186px;height:53px">CONTACT US</a>
  <svg class="abs" style="left:0;top:520px" width="1200" height="181" viewBox="0 0 1200 181">
    <path d="M0 181 C300 80 700 40 1200 20 L1200 181 Z" fill="#e3f0dd"/>
    <path d="M500 120 C750 70 950 50 1200 40 L1200 120 C950 100 750 110 500 120 Z" fill="#2c8a0c"/>
    <path d="M0 181 C350 110 750 90 1200 110 L1200 181 Z" fill="#fff"/>
  </svg>
</header>

<div class="seed-mark"></div>

<section>
  <div class="service on" style="left:77px">
    <div class="ic"><svg width="54" height="54" viewBox="0 0 54 54" fill="none" stroke="#fff" stroke-width="2"><rect x="6" y="8" width="42" height="34" rx="2"/><line x1="6" y1="15" x2="48" y2="15"/><polyline points="14,34 22,26 28,30 38,20"/></svg></div>
    <h3>Crop<br>Monitoring</h3>
    <p>Ensuring that you have real-time information to optimize irrigation management</p>
  </div>
  <div class="service" style="left:290px">
    <div class="ic"><svg width="54" height="54" viewBox="0 0 54 54" fill="none" stroke="#fff" stroke-width="2"><rect x="6" y="10" width="42" height="32" rx="2"/><line x1="6" y1="17" x2="48" y2="17"/><circle cx="24" cy="30" r="6"/><circle cx="36" cy="32" r="4"/></svg></div>
    <h3>Pump Monitoring<br>and Control</h3>
    <p>Scalable and cost-effective pump monitoring with built-in remote control</p>
  </div>
  <div class="service" style="left:499px">
    <div class="ic"><svg width="54" height="54" viewBox="0 0 54 54" fill="none" stroke="#fff" stroke-width="2"><rect x="10" y="6" width="34" height="42" rx="2"/><line x1="10" y1="14" x2="44" y2="14"/><circle cx="27" cy="31" r="10"/></svg></div>
    <h3>Irrigation<br>Automation</h3>
    <p>Upgrade your irrigation system: from retrofit to ranch - wide automation</p>
  </div>
  <div class="service" style="left:714px">
    <div class="ic"><svg width="54" height="54" viewBox="0 0 54 54" fill="none" stroke="#fff" stroke-width="2"><rect x="8" y="6" width="38" height="42" rx="2"/><line x1="14" y1="16" x2="40" y2="16"/><line x1="14" y1="24" x2="40" y2="24"/><line x1="14" y1="32" x2="40" y2="32"/><line x1="14" y1="40" x2="40" y2="40"/></svg></div>
    <h3>Control Panel<br>Design and Build</h3>
    <p>Leverage BLW design &amp; build expertise to meet your exact needs and specifications</p>
  </div>
  <div class="service" style="left:923px">
    <div class="ic"><svg width="54" height="54" viewBox="0 0 24 24" fill="none" stroke="#fff" stroke-width="1.2"><path d="M6 3h3l1.5 4-2 1.5a11 11 0 0 0 7 7L17 13.5l4 1.5v3a2 2 0 0 1-2 2A16 16 0 0 1 4 5a2 2 0 0 1 2-2z"/><path d="M14 3a7 7 0 0 1 7 7M14 6a4 4 0 0 1 4 4"/></svg></div>
    <h3>Contact Us</h3>
    <p>For immediate support call (555 014 - 2290)</p>
  </div>
</section>

<section>
  <h2 class="sec abs" style="left:98px;top:1236px">BLW IS SYSTEMS<br>INTEGRATOR</h2>
  <p class="lead abs" style="left:102px;top:1344px;width:400px">OUR GOAL: To Be your Trusted Partner for Technology Adoption</p>
  <p class="copy abs" style="left:102px;top:1414px;width:440px">Our focus is on helping California growers design, build and adopt effective irrigation management solutions.Our team has worked together for over 15 years, providing monitoring and control systems for 60+ crops that have successfully helped</p>
  <p class="copy abs" style="left:102px;top:1568px;width:440px">Over 500 farms significantly improve irrigation manage - ment. We also farm our own 200 acre technology lab to help ensure we deliver reliable monitoring &amp; automation to your farm.</p>
  <a class="btn" href="#" style="left:98px;top:1690px;width:166px;height:51px">PRODUCTS</a>
  <svg class="abs" style="left:830px;top:1212px" width="380" height="380"><circle cx="190" cy="190" r="155" fill="none" stroke="#d6e9cf" stroke-width="58"/></svg>
  <div class="ph" style="left:637px;top:1242px;width:288px;height:306px;background:linear-gradient(135deg,#4d5a3a,#7d8a5a 50%,#3e4a30)" role="img" aria-label="Almonds ripening on a branch"></div>
  <div class="ph" style="left:785px;top:1418px;width:286px;height:317px;background:linear-gradient(180deg,#a9c4e8 0%,#7faa2a 30%,#6f9a22 70%,#5b5a4a 100%)" role="img" aria-label="Young almond tree in an orchard"></div>
</section>

<section>
  <svg class="abs" style="left:-160px;top:1900px" width="460" height="460"><circle cx="240" cy="221" r="185" fill="none" stroke="#d6e9cf" stroke-width="78"/></svg>
  <div class="ph" style="left:126px;top:1877px;width:442px;height:334px;background:linear-gradient(180deg,#b9d4ee 0%,#c8d8e2 22%,#a89a78 35%,#6f8e3a 55%,#4f7a24 100%)" role="img" aria-label="Vineyard rows below dry hills"></div>
  <h2 class="sec abs" style="left:679px;top:1888px">WHY BLW?</h2>
  <p class="lead abs" style="left:683px;top:1945px">We're Your Local Field Tech Team.</p>
  <p class="copy abs" style="left:683px;top:1990px;width:385px">We are experts at deploying Information Technology for irrigation management. We partner with our customers to deliver the right solutions. Everything we sell is off-the-shelf, cost-effective and reliable</p>
  <a class="btn" href="#" style="left:679px;top:2143px;width:199px;height:53px">GET IN TOUCH</a>
</section>

<section>
  <svg class="abs" style="left:0;top:2240px" width="1200" height="520" viewBox="0 0 1200 520">
    <path d="M0 92 C400 50 850 30 1200 8 L1200 492 C900 498 650 520 420 498 C250 480 100 440 0 362 Z" fill="#2c8a0c"/>
  </svg>
  <div class="abs" style="left:0;top:2382px;width:1200px;display:flex;justify-content:center;align-items:center;gap:12px;color:#fff;font-size:36px;font-weight:400">
    <i style="width:24px;height:24px;border-radius:50%;background:#fff;display:block"></i>Stone Analytica
  </div>
  <h2 class="abs" style="top:2474px;width:1200px;text-align:center;color:#fff;font-size:40px;font-weight:600">STONE ANALYTICA</h2>
  <p class="abs" style="top:2538px;left:250px;width:700px;text-align:center;color:#fff;font-size:14px;line-height:27px">Stone Analytica is a cost-effective suite of tools built by Brook Ledger Works for irrigation management, providing farmers access to state-of-the-art industrial monitoring and control tools already widely adopted in other industries</p>

  <div class="abs" style="left:318px;top:2669px;width:110px;height:110px;border-radius:50%;background:#fff;box-shadow:0 4px 14px rgba(0,0,0,.15);display:flex;align-items:center;justify-content:center"><div style="width:96px;height:96px;border-radius:50%;background:var(--green);display:flex;align-items:center;justify-content:center"><svg width="54" height="54" viewBox="0 0 54 54" fill="none" stroke="#fff" stroke-width="2"><rect x="6" y="8" width="42" height="34" rx="2"/><line x1="6" y1="15" x2="48" y2="15"/><polyline points="14,34 22,26 28,30 38,20"/></svg></div></div>
  <div class="abs" style="left:544px;top:2673px;width:110px;height:110px;border-radius:50%;background:#fff;box-shadow:0 4px 14px rgba(0,0,0,.15);display:flex;align-items:center;justify-content:center"><svg width="60" height="60" viewBox="0 0 54 54" fill="none" stroke="#2c8a0c" stroke-width="2"><rect x="6" y="10" width="42" height="32" rx="2"/><line x1="6" y1="17" x2="48" y2="17"/><circle cx="24" cy="30" r="6"/><circle cx="36" cy="32" r="4"/></svg></div>
  <div class="abs" style="left:797px;top:2669px;width:110px;height:110px;border-radius:50%;background:#fff;box-shadow:0 4px 14px rgba(0,0,0,.15);display:flex;align-items:center;justify-content:center"><svg width="60" height="60" viewBox="0 0 54 54" fill="none" stroke="#2c8a0c" stroke-width="2"><rect x="10" y="6" width="34" height="42" rx="2"/><line x1="10" y1="14" x2="44" y2="14"/><circle cx="27" cy="31" r="10"/></svg></div>

  <p class="abs" style="left:273px;top:2798px;width:200px;text-align:center;font-size:15px;font-weight:500;line-height:24px">REMOTE CROP<br>MONITORING</p>
  <p class="abs" style="left:474px;top:2802px;width:250px;text-align:center;font-size:15px;font-weight:500;line-height:24px">REMOTE PUMP<br>MONITORING &amp; CONTROL</p>
  <p class="abs" style="left:752px;top:2798px;width:200px;text-align:center;font-size:15px;font-weight:500;line-height:24px">IRRIGATION<br>AUTOMATION</p>
</section>

<section>
  <div class="abs" style="left:0;top:3300px;width:1200px;height:342px;background:linear-gradient(180deg,#fff,#f1f6ee)"></div>
  <h2 class="sec abs" style="top:2914px;width:1200px;text-align:center;line-height:44px">WHAT IS REMOTE CROP<br>MONITORING ?</h2>
  <div class="ph" style="left:300px;top:3025px;width:594px;height:353px;background:linear-gradient(180deg,#6d7c86 0%,#8d9a88 25%,#b8b6a6 45%,#9d9786 100%)" role="img" aria-label="Solar-powered field sensor in a young orchard"></div>
  <svg class="abs" style="left:201px;top:3179px" width="58" height="58"><circle cx="29" cy="29" r="27" fill="#fff" stroke="#bbb" stroke-width="1.5"/><polyline points="33,19 23,29 33,39" fill="none" stroke="#bbb" stroke-width="2"/></svg>
  <svg class="abs" style="left:931px;top:3179px" width="58" height="58"><circle cx="29" cy="29" r="27" fill="#fff" stroke="#2c8a0c" stroke-width="1.5"/><polyline points="25,19 35,29 25,39" fill="none" stroke="#2c8a0c" stroke-width="2"/></svg>
  <p class="copy abs" style="left:280px;top:3402px;width:640px;text-align:center">Stone Analytica crop performance toolset starts with weather and soil moisture sensors that help farmers better manage crop health and irrigation efficiency.</p>
  <p class="copy abs" style="left:280px;top:3472px;width:640px;text-align:center">Stone Analytica gathers continuous, real-time data to provide insight on plant stress, infiltration, distribution uniformity, temperature, humidity, wind, rain and ET, making it the most valuable solution in the industry.</p>
</section>

<section>
  <h2 class="sec abs" style="top:3703px;width:1200px;text-align:center">PARTNERS</h2>
  <p class="abs" style="left:78px;top:3802px;color:var(--green);font-size:19px;font-weight:500">SOFTWARE</p>
  <p class="abs" style="left:621px;top:3802px;color:var(--green);font-size:19px;font-weight:500">SOIL MOISTURE SENSORS</p>
  <div class="abs" style="left:78px;top:3848px;width:503px;height:123px;border:1px solid #e3e3e3;display:flex;align-items:center;justify-content:space-around;padding:0 20px">
    <span style="width:160px;height:44px;background:#dde3e6;border-radius:4px;display:block"></span>
    <span style="width:44px;height:56px;background:#dde3e6;border-radius:4px;display:block"></span>
    <span style="width:160px;height:38px;background:#dde3e6;border-radius:4px;display:block"></span>
  </div>
  <div class="abs" style="left:619px;top:3848px;width:503px;height:123px;border:1px solid #e3e3e3;display:flex;align-items:center;justify-content:space-around;padding:0 20px">
    <span style="width:130px;height:44px;background:#dbe7f2;border-radius:4px;display:block"></span>
    <span style="width:130px;height:40px;background:#dde3e6;border-radius:4px;display:block"></span>
    <span style="width:150px;height:50px;background:#dbe7f2;border-radius:4px;display:block"></span>
  </div>
  <svg class="abs" style="left:30px;top:3892px" width="20" height="30"><polyline points="16,3 4,15 16,27" fill="none" stroke="#aaa" stroke-width="2"/></svg>
  <svg class="abs" style="left:1150px;top:3892px" width="20" height="30"><polyline points="4,3 16,15 4,27" fill="none" stroke="#aaa" stroke-width="2"/></svg>
</section>

<footer>
  <div class="abs" style="left:0;top:4015px;width:1200px;height:678px;background:linear-gradient(180deg,#3a4634 0%,#222a1f 40%,#151a13 100%)" role="img" aria-label="Farmland at dusk"></div>
  <svg class="abs" style="left:0;top:4010px" width="1200" height="170" viewBox="0 0 1200 170">
    <path d="M0 0 L1200 0 L1200 40 C800 70 400 100 0 170 Z" fill="#e3f0dd"/>
    <path d="M0 150 C350 80 800 50 1200 40 L1200 60 C800 70 350 100 0 165 Z" fill="#2c8a0c"/>
    <path d="M0 0 L1200 0 L1200 20 C800 40 400 70 0 130 Z" fill="#fff"/>
  </svg>
  <div class="abs" style="top:4250px;width:1200px;display:flex;justify-content:center;align-items:center;gap:10px;color:var(--green);font-size:32px;font-weight:600">
    <i style="width:22px;height:22px;border-radius:50%;background:var(--green);display:block"></i>BLW
  </div>
  <div class="abs" style="left:523px;top:4332px;display:flex;gap:8px">
    <span style="width:44px;height:44px;border-radius:50%;background:var(--green);display:block" aria-label="Social link"></span>
    <span style="width:44px;height:44px;border-radius:50%;background:var(--green);display:block" aria-label="Social link"></span>
    <span style="width:44px;height:44px;border-radius:50%;background:var(--green);display:block" aria-label="Social link"></span>
  </div>
  <div class="abs" style="left:209px;top:4412px;width:780px;height:104px;border:1px solid rgba(255,255,255,.35);display:flex;color:#fff;font-size:14px;line-height:24px">
    <div style="width:250px;border-right:1px solid rgba(255,255,255,.35);display:flex;align-items:center;gap:18px;padding-left:24px">
      <svg width="20" height="28" viewBox="0 0 20 28"><path d="M10 1a9 9 0 0 0-9 9c0 7 9 17 9 17s9-10 9-17a9 9 0 0 0-9-9z" fill="#2c8a0c"/><circle cx="10" cy="10" r="3.5" fill="#1c2419"/></svg>
      <span>Lorem ipsum simple<br>text print text.</span>
    </div>
    <div style="width:270px;border-right:1px solid rgba(255,255,255,.35);display:flex;align-items:center;gap:18px;padding-left:24px">
      <svg width="28" height="28" viewBox="0 0 24 24"><path d="M6 3h3l1.5 4-2 1.5a11 11 0 0 0 7 7L17 13.5l4 1.5v3a2 2 0 0 1-2 2A16 16 0 0 1 4 5a2 2 0 0 1 2-2z" fill="#2c8a0c"/></svg>
      <span>Phone :<br>555 014 - 2290</span>
    </div>
    <div style="flex:1;display:flex;align-items:center;gap:18px;padding-left:24px">
      <svg width="28" height="22" viewBox="0 0 28 22"><rect x="1" y="1" width="26" height="20" rx="2" fill="#2c8a0c"/><polyline points="2,3 14,12 26,3" fill="none" stroke="#1c2419" stroke-width="2"/></svg>
      <span>Email :<br>hello@brookledger.com</span>
    </div>
  </div>
  <p class="abs" style="top:4560px;width:1200px;text-align:center;color:#fff;font-size:14px;word-spacing:2px">Home &nbsp;|&nbsp; About &nbsp;|&nbsp; Why BLW? &nbsp;|&nbsp; Products &nbsp;|&nbsp; Partners &nbsp;|&nbsp; Contact</p>
  <p class="abs" style="top:4594px;width:1200px;text-align:center;color:#fff;font-size:14px">©BLW - 2020 All rights reserved.</p>
</footer>

</body>
</html>
```